Open Window; Sunrise Table, River Walk Rack Card

We want an additional 2 page (front and page) 3.67" x 8.5" rack card. This rack card is now the 2nd of the series . The first one is already completed/finalized and attached (Sunrise Table River Walk Rack Card PDF).
Use the text on the word document for the included Open Window Rack card. Please use the Sunrise Table River Walk Rack card as the template to mimic. We would like all subsequent rack cards to have a similar look and feel.
The document is for older readers. Do not put text over graphics and keep it simple and easy to read with high contrast.
We want some very simple design element(s) incorporated that convey Native American communities or heritage. But NO headdress, teepee graphics, etc. At the top, of the first page we would like a collage of healthy food images. This can include fish, chicken, fresh vegetables, berries, brown rice, etc. Please remember to include the funding statement - it can be in a very small font 6/7 point. For more information about our project, please visit https://pelmorvo.org/kite-lane/

```html
<!DOCTYPE html>
<html lang="en">
<head>
<meta charset="utf-8">
<title>Sunrise Table River Walk – Open Window Rack Card</title>
<link href="https://fonts.googleapis.com/css2?family=Montserrat:wght@400;500;600;700;800&display=swap" rel="stylesheet">
<style>
:root{
  --bg:#676668;
  --paper:#fbfbfa;
  --maroon:#5c1d1a;
  --teal:#4aa3a8;
  --teal-dark:#1e6366;
  --teal-band:#2e7d80;
  --ink:#1a1a1a;
  --tick:#d9535a;
}
*{margin:0;padding:0;box-sizing:border-box}
html,body{width:1200px;height:1200px;overflow:hidden}
body{background:var(--bg);font-family:"Montserrat",Arial,sans-serif;color:var(--ink);position:relative}
.card{position:absolute;top:60px;width:466px;height:1080px;background:var(--paper);overflow:hidden}
.card--front{left:92px}
.card--back{left:643px}
.abs{position:absolute}

/* front */
.food-plate{left:-10px;top:0;width:170px;height:130px;border-radius:0 0 85px 85px;background:radial-gradient(circle at 50% 45%,#e8b24a,#c7522f 45%,#4f7d2f 75%,#e9e6e0 76%)}
.food-berries{left:170px;top:18px;width:128px;height:108px;border-radius:50% 50% 45% 45%;background:radial-gradient(circle at 50% 50%,#b0202d 30%,#1f2540 34%,#2b3358 70%,#e8e6e2 72%)}
.food-salad{left:312px;top:0;width:170px;height:128px;border-radius:0 0 85px 85px;background:radial-gradient(circle at 45% 45%,#d39b3c,#8ab04a 40%,#4f7d2f 72%,#e9e6e0 74%)}

.headline{left:31px;top:150px;font-weight:800;font-size:49px;line-height:45px;letter-spacing:-.5px;text-transform:uppercase}
.headline span{display:block}
.headline .l1{color:var(--maroon)}
.headline .l2{color:var(--teal)}
.headline .l3{color:#000}

.intro{left:34px;top:295px;width:402px;font-size:14.3px;line-height:18.5px;font-weight:500;text-align:justify;letter-spacing:-.1px}
.subhead{left:34px;top:375px;font-size:17px;font-weight:700;color:var(--teal-dark);letter-spacing:-.2px}
.subhead em{font-style:normal;color:var(--maroon)}

.checklist{list-style:none}
.checklist li{position:relative;padding-left:27px;margin-bottom:7px;font-size:15.5px;line-height:19.3px;font-weight:500;letter-spacing:-.2px}
.checklist li svg{position:absolute;left:0;top:3px;width:14px;height:14px}
.front-list{left:36px;top:404px;width:400px}

.pattern-band{height:24px;background:linear-gradient(180deg,#9bbcbd,#b58b86)}
.front-pattern{left:0;top:804px;width:466px;height:25px}
.doctor-band{left:0;top:829px;width:466px;height:56px;background:var(--maroon);color:#fff;font-weight:700;font-size:12.8px;line-height:17px;text-transform:uppercase;padding:12px 0 0 35px;letter-spacing:-.1px}

.quote-mark{left:34px;top:888px;font-size:40px;line-height:36px;font-weight:800;color:var(--teal)}
.quote{left:36px;top:909px;width:290px;font-size:13.8px;line-height:18px;font-weight:700;color:#222;letter-spacing:-.3px;white-space:nowrap}
.quote .close{color:var(--teal);font-size:24px;line-height:0;font-weight:800}
.quote-name{left:36px;top:967px;font-size:12px;font-weight:600;letter-spacing:-.2px}
.fruit-bowl{left:333px;top:888px;width:124px;height:124px;border-radius:50%;background:radial-gradient(circle at 50% 50%,#e8a53a,#c93a2f 50%,#7ba24a 70%,#f1efea 73%);box-shadow:0 4px 8px rgba(0,0,0,.2);z-index:2}
.goal-band{left:0;top:993px;width:466px;height:40px;background:var(--teal-band);color:#fff;font-size:12.5px;line-height:16.5px;font-weight:700;padding:4px 0 0 37px;letter-spacing:-.3px}

.funding{left:37px;top:1040px;width:400px;font-size:6.5px;line-height:8.3px;font-weight:500;color:#222}

/* back */
.make-title{left:35px;top:36px;font-size:35px;line-height:40px;font-weight:800;letter-spacing:-.6px;color:var(--maroon);text-transform:uppercase;white-space:nowrap}
.make-title em{font-style:normal;color:var(--teal-dark)}
.recipe-name{left:36px;top:88px;font-size:15.5px;line-height:21.5px;font-weight:700;color:var(--teal-dark);letter-spacing:-.2px}
.bean-bowl{left:29px;top:161px;width:167px;height:117px;border-radius:40% 40% 50% 50%/30% 30% 70% 70%;background:radial-gradient(ellipse at 50% 25%,#efe4c4 25%,#8a4a24 32%,#5a2c14 80%);box-shadow:0 10px 10px -6px rgba(0,0,0,.25)}
.ing-head{left:227px;top:88px;font-size:16px;font-weight:700;color:var(--maroon);letter-spacing:-.2px}
.ing-list{left:226px;top:113px;width:215px}
.ing-list li{font-size:15.5px;line-height:17.6px;padding-left:24px;margin-bottom:3.5px}
.ing-list li svg{top:1px}
.method{left:32px;top:336px;width:403px;font-size:13.9px;line-height:20.3px;font-weight:500;text-align:justify;letter-spacing:-.15px}
.yield{left:32px;top:501px;font-size:15.5px;font-weight:700;color:var(--teal-dark)}
.elders-band{left:0;top:546px;width:466px;height:135px;background:var(--maroon);color:#fff;font-size:13.8px;line-height:21.1px;font-weight:700;text-transform:uppercase;padding:22px 34px 0;text-align:justify;letter-spacing:-.1px}
.back-pattern{left:0;top:681px;width:466px;height:22px}
.more-title{left:0;top:727px;width:466px;text-align:center;font-size:27px;font-weight:800;color:var(--maroon);text-transform:uppercase;letter-spacing:-.4px}
.more-sub{left:0;top:762px;width:466px;text-align:center;font-size:22px;font-weight:800;color:var(--teal-dark);text-transform:uppercase;letter-spacing:-.3px}
.source{left:0;width:466px;text-align:center}
.source .org{font-size:16px;font-weight:700;color:var(--maroon);text-transform:uppercase;letter-spacing:-.2px}
.source .url{font-size:16px;font-weight:500;color:#111;letter-spacing:-.2px}
.source--one{top:814px}
.source--two{top:875px}
.brand{left:100px;top:945px;display:flex;align-items:center;gap:14px}
.brand-dot{width:64px;height:64px;border-radius:50%;background:var(--teal)}
.brand-name{font-size:19px;font-weight:700;color:var(--teal);line-height:22px}
.funding--back{left:36px}
</style>
</head>
<body>
<svg width="0" height="0" style="position:absolute">
  <defs>
    <symbol id="tick" viewBox="0 0 14 14">
      <rect x="1" y="2.5" width="10.5" height="10.5" rx="1.5" fill="none" stroke="#d9535a" stroke-width="1.5"/>
      <path d="M3.5 7.5l2.6 2.6L13 2.5" fill="none" stroke="#d9535a" stroke-width="2" stroke-linecap="round" stroke-linejoin="round"/>
    </symbol>
  </defs>
</svg>

<section class="card card--front">
  <div class="abs food-plate" role="img" aria-label="Plate of grilled chicken, corn, peppers, avocado and cucumber"></div>
  <div class="abs food-berries" role="img" aria-label="Heart-shaped dish of blueberries and pomegranate seeds"></div>
  <div class="abs food-salad" role="img" aria-label="Bowl of salad with avocado, tomato and chicken"></div>

  <h1 class="abs headline">
    <span class="l1">Sunrise Table</span>
    <span class="l2">River Walk</span>
    <span class="l3">Open Window</span>
  </h1>

  <p class="abs intro">Making small changes in what and how you eat can make you feel better and stay healthier longer. Healthy food choices may be good for your brain, energy, mood, and health.</p>

  <h2 class="abs subhead">Little changes that make a <em>big difference:</em></h2>

  <ul class="abs checklist front-list">
    <li><svg><use href="#tick"/></svg>Start today!</li>
    <li><svg><use href="#tick"/></svg>Write down what, when, and how much you eat for three days</li>
    <li><svg><use href="#tick"/></svg>Set SMART goals (Specific, Measurable, Attainable, Relevant &amp; Timebound), like: “I will eat one piece of fruit at breakfast three times this week.”</li>
    <li><svg><use href="#tick"/></svg>Make just 1 or 2 changes at a time until they become a habit</li>
    <li><svg><use href="#tick"/></svg>Focus more on eating healthy food versus not eating unhealthy food</li>
    <li><svg><use href="#tick"/></svg>Make a game plan for the times you get tempted to eat unhealthy foods</li>
    <li><svg><use href="#tick"/></svg>Involve the whole family in setting goals</li>
    <li><svg><use href="#tick"/></svg>Name your main reason to eat healthier and feel better, like “More energy to go to church and tribal cultural events.”</li>
  </ul>

  <div class="abs pattern-band front-pattern" role="img" aria-label="Zigzag band in teal and rose"></div>
  <p class="abs doctor-band">Talk to your doctor about healthier eating to<br>make you feel better and stay healthier longer.</p>

  <div class="abs quote-mark">“</div>
  <p class="abs quote">When it comes to traditional<br>foods, for me it’s something more<br>than just food, it’s my heritage.<span class="close">”</span></p>
  <p class="abs quote-name">Marisol Tenney (Desert River Nation)</p>
  <div class="abs fruit-bowl" role="img" aria-label="Bowl of mixed fresh fruit"></div>
  <p class="abs goal-band">Making small, practical changes can help<br>you achieve your health goals.</p>

  <p class="abs funding">This product is supported by the Regional Health Fund (RHF) of the Northfield Department of Community Wellness (NDCW) as part of a financial assistance award totaling $348,711 with 100 percent funded by RHF/NDCW. The contents are those of the author(s) and do not necessarily represent the official views of, nor an endorsement, by RHF/NDCW, or the Northfield Government.</p>
</section>

<section class="card card--back">
  <h2 class="abs make-title">Make This <em>At Home</em></h2>
  <h3 class="abs recipe-name">O’odham White<br>Tepary Bean Stew</h3>
  <div class="abs bean-bowl" role="img" aria-label="Wooden bowl of tepary bean stew with meat"></div>

  <h3 class="abs ing-head">Ingredients</h3>
  <ul class="abs checklist ing-list">
    <li><svg><use href="#tick"/></svg>1 cup dried tepary beans, rinsed &amp; picked through (substitute Navy Beans or Great Northern beans)</li>
    <li><svg><use href="#tick"/></svg>10 cups of water</li>
    <li><svg><use href="#tick"/></svg>1 tsp. salt</li>
    <li><svg><use href="#tick"/></svg>1 lb. oxtails, beef short ribs, deer, rabbit, or chicken</li>
  </ul>

  <p class="abs method">Put beans, water, and salt in a stockpot. Bring to a boil, reduce heat and simmer, covered, for one hour and a half. Add meat to the bean mixture, cover and cook for one more hour, or until beans are tender and meat is falling off the bone. If using a crockpot, place water and all other ingredients in the pot, cover, and set to high. Cook for 8 hours or until the meat is falling off the bone and the beans are tender.</p>
  <p class="abs yield">Makes 8 – 10 cups.</p>

  <p class="abs elders-band">Elders are our keepers of traditional knowledge about food and ways of life. You play an important role in sharing this knowledge with younger generations.</p>
  <div class="abs pattern-band back-pattern" role="img" aria-label="Zigzag band in teal and rose"></div>

  <h2 class="abs more-title">For More Information</h2>
  <h3 class="abs more-sub">About Goal Setting</h3>

  <div class="abs source source--one">
    <p class="org">Hollow Creek Nutrition Council</p>
    <p class="url">https://qlnk.co/PlateGoalVideo</p>
  </div>
  <div class="abs source source--two">
    <p class="org">Aldergate Health</p>
    <p class="url">https://qlnk.co/AldergateGoals</p>
  </div>

  <div class="abs brand">
    <span class="brand-dot"></span>
    <span class="brand-name">Kite Lane<br>Resource Center</span>
  </div>

  <p class="abs funding funding--back">This product is supported by the Regional Health Fund (RHF) of the Northfield Department of Community Wellness (NDCW) as part of a financial assistance award totaling $348,711 with 100 percent funded by RHF/NDCW. The contents are those of the author(s) and do not necessarily represent the official views of, nor an endorsement, by RHF/NDCW, or the Northfield Government.</p>
</section>
</body>
</html>
```